Advertisement Design Project

I would like to have some advertisement ideas to promote my business. Our company provides credit repair, tax preparation, notary service, ledger preparation (for small businesses and independent contractors) tax restoration (help people with liens, levy, garnishments, etc. by negotiating with the DQV in these matters)

The name of our company is Tamberly Financing
Our "Jubilatrix" program focuses on tax preparation, restoration, and credit repair.
Our "Maple Step" program prepares ledgers for small business and independent contractors by preparing monthly ledgers so that at tax season they are not having to look everywhere for their receipts in order to get all deductions due to them during the tax season.

We need something that is catchy and will gain attention

attached is our logo. Our slogan is "Happiness, Restored!"

Thank you!

Target Market(s)

The financially distressed
Small business owners
Independent contractors
businesses that rely on credit worthy clients to do business with

Industry/Entity Type

Small Business

Requirements
Must have
• great pictures
nice layout

```html
<!DOCTYPE html>
<html lang="en">
<head>
<meta charset="utf-8">
<title>Tamberly Financing – Flyer</title>
<link rel="stylesheet" href="https://fonts.googleapis.com/css2?family=Source+Sans+3:wght@400;600&display=swap">
<style>
  :root {
    --page-bg: #cfcfcf;
    --flyer-black: #000000;
    --brand-blue: #4aa6d6;
    --swoosh-deep: #1f78b8;
    --slogan-grey: #c8c8c8;
    --text-white: #ffffff;
    --logo-navy: #1d3a66;
    --photo-border: #ffffff;
  }
  * { margin: 0; padding: 0; box-sizing: border-box; }
  html, body {
    width: 1200px; height: 896px; overflow: hidden;
    background: var(--page-bg);
    font-family: "Source Sans 3", "Myriad Pro", Arial, sans-serif;
  }
  .flyer {
    position: absolute; left: 40px; top: 31px;
    width: 1120px; height: 834px;
    background: var(--flyer-black);
    overflow: hidden;
    color: var(--text-white);
  }
  .flyer-shapes { position: absolute; inset: 0; width: 100%; height: 100%; }
  .flyer-overlay { pointer-events: none; }

  .brand-title {
    position: absolute; left: 381px; top: 16px;
    font-size: 52px; font-weight: 400; color: var(--brand-blue);
    line-height: 64px; white-space: nowrap;
  }
  .brand-slogan {
    position: absolute; left: 383px; top: 84px;
    font-size: 28px; line-height: 34px; color: var(--slogan-grey);
  }
  .brand-mark {
    position: absolute; left: 918px; top: 11px;
    width: 183px; height: 175px;
    background: var(--logo-navy);
    border: 6px solid var(--photo-border);
    display: flex; align-items: center; justify-content: center;
    text-align: center;
    font-size: 22px; font-weight: 400; color: var(--text-white);
    line-height: 1.2; padding: 10px;
  }

  .program {
    position: absolute; left: 290px; top: 214px;
    font-size: 28px; line-height: 34.5px; white-space: nowrap;
  }
  .program h2 { font-size: 30px; font-weight: 400; line-height: 40px; }

  .services {
    position: absolute; left: 688px; top: 196px;
    font-size: 27px; line-height: 34.5px; white-space: nowrap;
  }
  .services h2 { font-size: 46px; font-weight: 400; line-height: 56px; margin-bottom: 16px; }
  .services ul { list-style: none; }

  .photo {
    position: absolute;
    border: 4px solid var(--photo-border);
  }
  .photo-tax-time {
    left: 4px; top: 315px; width: 267px; height: 175px;
    background: linear-gradient(135deg, #cfcab8, #7f8d78 45%, #e9e0b8 75%, #bfc4c6);
  }
  .photo-dollar-figure {
    left: 4px; top: 500px; width: 263px; height: 200px;
    background: radial-gradient(circle at 55% 45%, #6fb9d6, #d7ecf4 70%);
  }
  .photo-handshake {
    left: 273px; top: 381px; width: 392px; height: 263px;
    background: linear-gradient(160deg, #f2f2f2, #e0dcd6 50%, #2a3145 100%);
    border-width: 6px;
  }
  .photo-notary-stamp {
    left: 528px; top: 619px; width: 416px; height: 190px;
    background: linear-gradient(120deg, #4d565f, #b9bfc5 50%, #f3f1ee);
    border-width: 6px;
  }

  .contact-label {
    position: absolute; left: 151px; top: 700px;
    font-size: 19px; line-height: 24px; color: var(--text-white);
  }
</style>
</head>
<body>
  <main class="flyer">
    <svg class="flyer-shapes" viewBox="0 0 1120 834" aria-hidden="true">
      <defs>
        <linearGradient id="cornerGrey" x1="0" y1="0" x2="1" y2="1">
          <stop offset="0" stop-color="#6e6e6e"/>
          <stop offset="1" stop-color="#111111"/>
        </linearGradient>
        <linearGradient id="cornerBlue" x1="0" y1="1" x2="1" y2="0">
          <stop offset="0" stop-color="#2f8fc4"/>
          <stop offset="1" stop-color="#9ad6ee"/>
        </linearGradient>
      </defs>
      <path class="corner-fill" d="M0,0 L380,0 C220,30 60,120 0,330 Z" fill="url(#cornerGrey)"/>
      <path class="corner-swoosh" d="M380,14 C220,40 50,140 0,360 L0,320 C50,120 210,30 380,14 Z" fill="url(#cornerBlue)"/>
    </svg>

    <h1 class="brand-title">Tamberly Financing</h1>
    <p class="brand-slogan">Happiness, Restored!</p>
    <div class="brand-mark">Tamberly Financing</div>

    <section class="program">
      <h2>"Jubilatrix" program</h2>
      <p>Tax preparation<br>Restoration<br>and credit repair.</p>
    </section>

    <section class="services">
      <h2>Company provides</h2>
      <ul>
        <li>credit repair</li>
        <li>tax preparation</li>
        <li>notary service</li>
        <li>ledger preparation</li>
        <li>tax restoration (help people<br>with liens, levy, garnishments, etc.<br>by negotiating with the DQV in<br>these matters)</li>
      </ul>
    </section>

    <div class="photo photo-tax-time" role="img" aria-label="Photo of cash, a calculator and a tax time sticky note"></div>
    <div class="photo photo-dollar-figure" role="img" aria-label="Illustration of a small figure pushing a large blue dollar sign"></div>
    <div class="photo photo-handshake" role="img" aria-label="Photo of a couple shaking hands with a financial advisor"></div>
    <div class="photo photo-notary-stamp" role="img" aria-label="Photo of a hand using a notary stamp beside a laptop"></div>

    <svg class="flyer-shapes flyer-overlay" viewBox="0 0 1120 834" aria-hidden="true">
      <defs>
        <linearGradient id="bottomGrey" x1="0" y1="0" x2="0" y2="1">
          <stop offset="0" stop-color="#2a2a2a"/>
          <stop offset="1" stop-color="#a8a8a8"/>
        </linearGradient>
        <linearGradient id="swooshBlue" x1="0" y1="1" x2="1" y2="0">
          <stop offset="0" stop-color="#e6f6fb"/>
          <stop offset="0.5" stop-color="#8fd0ea"/>
          <stop offset="1" stop-color="#2f8fc4"/>
        </linearGradient>
      </defs>
      <path class="bottom-fill" d="M0,716 C180,668 360,670 520,720 C600,745 640,770 560,834 L0,834 Z" fill="url(#bottomGrey)"/>
      <path class="bottom-line" d="M0,716 C180,668 360,670 520,720 C620,752 700,800 760,834" fill="none" stroke="var(--swoosh-deep)" stroke-width="6"/>
      <path class="main-swoosh" d="M330,834 C720,840 1050,700 1120,330 L1120,460 C1060,720 860,834 640,834 Z" fill="url(#swooshBlue)"/>
    </svg>

    <p class="contact-label">CONTACT</p>
  </main>
</body>
</html>
```